Firm of surveyors needs a professional yet friendly looking flyer

Our company offers help to landlords who have a phone mast on their property. We help them to negotiate the best rent and lease terms. There are so many landlords who don't seek professional advice because they don't know it's available. We want to send them a flyer which is informative, looks professional but also friendly so it prompts them to call us. I have attached the wording and some pictures but have more I can send but they were too large to attach.

Target Market(s)

Ranges from farmers to large corporations and land owners

Industry/Entity Type

Surveyor

Font styles to use
Sans Serif

Colors
acd136
9bcb3c
000000
ffffff
606060
848484

Requirements
Must have
• Must be clear, must give a professional look, must include pictures, must include our logo, must use our colour scheme (or variations of it). Ideally, I would like a try-fold design if possible.
Nice to have
• I would like there to be stand out lines to catch the readers eye (I have included some on the wording document). I would like a clean and modern design
Should not have
• Should not be too fussy

```html
<!DOCTYPE html>
<html lang="en">
<head>
<meta charset="utf-8">
<title>Masthead Lease Partners – Landlord Flyer</title>
<link rel="stylesheet" href="https://fonts.googleapis.com/css2?family=Didact+Gothic&family=Montserrat:wght@700&display=swap">
<style>
  :root{
    --green-dark:#2f6b1e;
    --green:#8cbf2f;
    --green-light:#acd136;
    --green-mid:#9bcb3c;
    --black:#222222;
    --ink:#3a3a3a;
    --blue:#2a6bb8;
    --blue-light:#4b8fd6;
    --paper:#ffffff;
    --backdrop:#e4e4e4;
  }
  *{box-sizing:border-box;margin:0;padding:0}
  html,body{width:1200px;height:798px;overflow:hidden;background:var(--backdrop)}
  body{font-family:"Didact Gothic",sans-serif;color:var(--ink)}
  .flyer{position:absolute;left:83px;top:0;width:1034px;height:798px;background:var(--paper);display:flex}
  .panel{position:relative;height:100%}
  .panel--left{width:338px}
  .panel--middle{width:348px}
  .panel--right{width:348px}
  .copy{position:absolute;font-size:12.6px;line-height:15.6px}
  .panel--left .copy{left:33px;top:28px;width:290px}
  .panel--middle .copy{left:27px;top:28px;width:294px;text-align:justify;text-align-last:center}
  .panel--right .copy{left:20px;top:28px;width:297px;text-align:right}
  .copy p{margin-bottom:15.6px}
  .brand-title{font-family:"Montserrat",sans-serif;font-weight:700;color:var(--green-dark);font-size:18.5px;line-height:20px;letter-spacing:.2px}
  .intro-title{font-family:"Montserrat",sans-serif;font-weight:700;color:var(--green);font-size:15px;line-height:18.5px;margin-bottom:1px}
  .highlight{font-family:"Montserrat",sans-serif;font-weight:700;color:var(--green);font-size:12px;line-height:15.6px}
  .section-title{font-family:"Montserrat",sans-serif;font-weight:700;color:var(--green);font-size:15px;line-height:17px;text-align:center;text-align-last:center;margin-bottom:1px}
  .panel--right .section-title{text-align:right;text-align-last:right}
  .callout{font-family:"Montserrat",sans-serif;font-weight:700;color:var(--green);font-size:12.4px;line-height:15.6px}
  .accent-bar{position:absolute;left:0;width:100%;height:14px;background:var(--green-mid)}
  .accent-bar--top{top:0}
  .accent-bar--bottom{bottom:0}
  .mast-graphic{position:absolute;left:0;bottom:0;width:100%;height:270px;display:block}
</style>
</head>
<body>
<main class="flyer">
  <section class="panel panel--left">
    <div class="copy">
      <h1 class="brand-title">MASTHEAD LEASE PARTNERS</h1>
      <h2 class="intro-title">IS A FIRM OF TELECOMS SURVEYORS WITH OVER 15 YEARS’ EXPERIENCE OF DEALING WITH MOBILE PHONE MAST OPERATORS.</h2>
      <p>We have built up a massive database of thousands of comparable mobile phone mast deals to aid us in our telecoms negotiations. All our surveyors have spent time working for phone mast operators and know the industry inside out. We now work exclusively for landlords, fighting your corner, ensuring our landlords get the highest rents and best lease terms available in the market place.</p>
      <p>Many of the original mobile phone mast leases / agreements are now coming up for renewal. This is an ideal opportunity for landlords to achieve the best deal. <span class="highlight">WE ARE CURRENTLY OFFERING TO REVIEW TELECOMS LEASES FOR FREE AND PROVIDE LANDLORDS WITH OUR RECOMMENDATIONS.</span> If you would like to take us up on this free no obligation offer, send a copy of your agreement and any recent correspondence to us, either via post or email using the details on this flyer.</p>
    </div>
    <svg class="mast-graphic" viewBox="0 0 325 260" preserveAspectRatio="none">
      <polygon points="0,8 325,140 325,215 0,68" fill="var(--black)"/>
      <g role="img" aria-label="Photo of a mobile phone mast with antennas against a blue sky">
        <defs><linearGradient id="skyLeft" x1="0" y1="0" x2="1" y2="1"><stop offset="0" stop-color="var(--blue-light)"/><stop offset="1" stop-color="var(--blue)"/></linearGradient></defs>
        <polygon points="0,74 325,222 325,260 0,260" fill="url(#skyLeft)"/>
      </g>
      <polygon points="60,0 325,108 325,124 60,16" fill="var(--green-light)"/>
      <polygon points="90,22 325,118 325,134 90,38" fill="var(--green)"/>
    </svg>
  </section>

  <section class="panel panel--middle">
    <div class="accent-bar accent-bar--top"></div>
    <div class="copy">
      <p>Please also provide us with your name, contact number and let us know the current rent you are achieving so we can see if there is room for improvement. Once we have received this, one of our surveyors will give you a call when convenient to talk through your lease with you, highlighting anything we feel needs addressing, any opportunity to increase the rent, or to discuss a specific issue you are having with your mast <em>(i.e. an upgrade request)</em>.</p>
      <p>Recently, operators have been attempting to cut costs by reducing rents. They are joining forces in an effort to drive rents down. Many landlords are contacting us after receiving a letter from the operators / operator’s agent, telling them they must accept a rent reduction or risk losing their site. In the majority of cases, Masthead Lease Partners can prevent this from occurring and protect the landlord’s rental income.</p>
      <h2 class="section-title">SELL YOUR PHONE MAST</h2>
      <p>We can also assist landlords in selling their phone mast. We have strong links with many large investors who regularly purchase the freehold or leasehold interest of masts and will pay a cash lump sum of tens, even hundreds of thousands of pounds. This can be done in a matter of weeks and the cash is yours to spend however you like, regardless of whether the mast stays for the duration of the investors leasehold or not. We can negotiate flexible terms, such as a buy-back option so please call us today to discuss.</p>
      <h2 class="section-title">GETTING A PHONE MAST</h2>
      <p>If you don’t currently have a mast located on your land but are interested in receiving thousands of pounds a year in rental income, or you have a redundant mast you would like to market, we offer a free advertising service on our website. We will market your land to phone mast operators with a view to having a mast located there. Please visit the ‘Advertise My Site’ link on our website to take advantage of this service.</p>
    </div>
    <div class="accent-bar accent-bar--bottom"></div>
  </section>

  <section class="panel panel--right">
    <div class="copy">
      <h2 class="section-title">THE CURRENT TELECOMS CLIMATE</h2>
      <p>The telecoms market, in relation to mobile phone masts, is going through some huge changes. Operators are combining to cut costs. We have already seen Northline join forces with Telvo and Aircell form a jointly owned company with Vocom called JMIL. More recently, Telvo and Brightwave have merged to form Allconnect Ltd to become the new network leader. What this can mean for the landlord is changes to their site and potentially the loss of income. It can all be very confusing but don’t worry, this is where we can help. We know the telecoms industry and understand how a new situation may affect a landlord, therefore, allowing us to provide the best advice on protecting your asset.</p>
      <p>In April 2017, the Government introduced the Digital Economy Act. This sets out significant changes for landlords, including the way rents are calculated. We have already seen operators contact landlords, trying to reduce their rent in light of this new law. We are working alongside specialist telecoms solicitors to try to reduce the potential negative impact on landlords.</p>
      <p class="callout">LANDLORDS SHOULD NOT SIGN ANYTHING UNTIL THEY HAVE SOUGHT PROFESSIONAL ADVICE</p>
    </div>
    <svg class="mast-graphic" viewBox="0 0 325 260" preserveAspectRatio="none">
      <g transform="translate(325,0) scale(-1,1)">
        <polygon points="0,8 325,140 325,215 0,68" fill="var(--black)"/>
        <g role="img" aria-label="Photo of a telecoms tower platform with antennas against a blue sky">
          <defs><linearGradient id="skyRight" x1="1" y1="0" x2="0" y2="1"><stop offset="0" stop-color="var(--blue-light)"/><stop offset="1" stop-color="var(--blue)"/></linearGradient></defs>
          <polygon points="0,74 325,222 325,260 0,260" fill="url(#skyRight)"/>
        </g>
        <polygon points="60,0 325,108 325,124 60,16" fill="var(--green-light)"/>
        <polygon points="90,22 325,118 325,134 90,38" fill="var(--green)"/>
      </g>
    </svg>
  </section>
</main>
</body>
</html>
```